New icons designed for home page

We are a charitable buy and sell site. A % of everything sold on the site goes to a charity. We need new icons for home page as it's looking a bit plain. We would like them to be simple but very catchy. The current ones are simply too generic so please make our home page look great! Image attached of the four icons we need replaced. Buy, Shop, Causes and Stores need new icon images and font please. Design brief is for all four icons to be designed as well the new font for the text.
You can see more of the site here www.givlomart.com

Target Market(s)

People who buy and sell 2nd hand items. Charity givers. Market stall holders/shoppers

Industry/Entity Type

Online Store

Requirements
Must have
• Individualism. Congruent and beautiful. Color match with our current site/logo colors.

```html
<!DOCTYPE html>
<html lang="en">
<head>
<meta charset="utf-8">
<title>Givlomart – Shop. Sell. Donate.</title>
<link rel="stylesheet" href="https://fonts.googleapis.com/css2?family=Mulish:wght@400;600;800&family=Open+Sans:wght@400&display=swap">
<style>
:root{
  --ink:#2f2f2f;
  --muted:#555;
  --teal:#1b8a78;
  --red:#e5242b;
  --blue:#3b5e8c;
  --nav-bg:#f3f3f3;
  --line:#dcdcdc;
  --white:#fff;
  --badge:#111;
}
*{box-sizing:border-box;margin:0;padding:0}
html,body{width:1200px;height:785px;overflow:hidden;background:var(--white)}
body{position:relative;font-family:"Mulish",sans-serif;color:var(--ink)}
.abs{position:absolute}

.brand{left:80px;top:6px;text-align:center}
.brand-name{font-size:44px;font-weight:800;letter-spacing:-1px;line-height:48px;color:var(--ink)}
.brand-tag{font-size:13px;font-weight:600;color:var(--ink);margin-top:-2px}

.search{left:342px;top:17px;width:270px;height:34px;border:1px solid var(--line);display:flex}
.search-input{flex:1;font-size:16px;color:#888;padding:7px 14px}
.search-btn{width:33px;background:var(--teal);display:flex;align-items:center;justify-content:center}

.store-badge{top:19px;height:29px;background:var(--badge);border-radius:4px}
.header-link{top:24px;font-size:15px;color:var(--teal)}
.sell-btn{left:1097px;top:14px;width:73px;height:41px;background:var(--teal);border-radius:4px;color:var(--white);font-size:15px;display:flex;align-items:center;justify-content:center;gap:7px}

.catnav{left:0;top:74px;width:1200px;height:39px;background:var(--nav-bg);border-top:1px solid #e6e6e6;border-bottom:1px solid #e6e6e6}
.catnav-item{top:0;height:37px;line-height:37px;font-size:15px;color:var(--muted);text-align:center;border-left:1px solid var(--line)}
.catnav-item.last{border-right:1px solid var(--line)}
.tally{right:30px;top:0;line-height:37px;font-size:14px;color:var(--ink)}
.tally b{color:var(--red);font-weight:400}

.hero{left:0;top:113px;width:1200px;height:376px;background:radial-gradient(ellipse at 52% 60%,#e4ddd4 0%,#d4d0cb 45%,#c9c6c2 100%)}
.hero-title{left:0;top:258px;width:1200px;text-align:center;font-size:42px;font-weight:400;color:#111}
.hero-sub{left:0;top:318px;width:1200px;text-align:center;font-size:22px;color:#111}

.get-started{left:0;top:515px;width:1200px;text-align:center;font-size:24px}
.action{top:552px;width:200px;text-align:center}
.action svg{display:block;margin:0 auto;height:92px}
.action-label{font-family:"Open Sans",sans-serif;font-size:21px;margin-top:8px;line-height:26px}

.choose{left:65px;top:670px;font-size:22px}

.cause{top:736px;font-size:13px;font-weight:800;text-align:center;width:110px}
.more{left:1073px;top:736px;font-size:17px;display:flex;align-items:center;gap:6px}
</style>
</head>
<body>

<header>
  <div class="abs brand">
    <div class="brand-name">givlomart</div>
    <div class="brand-tag">Shop. Sell. Donate.</div>
  </div>

  <div class="abs search">
    <div class="search-input">What are you looking for?</div>
    <div class="search-btn">
      <svg width="16" height="16" viewBox="0 0 16 16"><circle cx="6.5" cy="6.5" r="4.8" fill="none" stroke="#fff" stroke-width="2.2"/><line x1="10" y1="10" x2="14.5" y2="14.5" stroke="#fff" stroke-width="2.6" stroke-linecap="round"/></svg>
    </div>
  </div>

  <div class="abs store-badge" style="left:757px;width:90px"></div>
  <div class="abs store-badge" style="left:852px;width:90px"></div>

  <a class="abs header-link" style="left:963px">Login</a>
  <a class="abs header-link" style="left:1024px">Sign up</a>
  <div class="abs sell-btn">
    <svg width="15" height="13" viewBox="0 0 15 13"><rect x="0" y="2.5" width="15" height="10.5" rx="1.5" fill="#fff"/><rect x="4.5" y="0.5" width="6" height="3" fill="#fff"/><circle cx="7.5" cy="7.5" r="3" fill="var(--teal)"/></svg>
    Sell
  </div>
</header>

<nav class="abs catnav">
  <div class="abs catnav-item" style="left:67px;width:96px">Clothing</div>
  <div class="abs catnav-item" style="left:163px;width:218px">Electronics and Computer</div>
  <div class="abs catnav-item" style="left:381px;width:164px">Home and Garden</div>
  <div class="abs catnav-item" style="left:545px;width:160px">More categories <span style="font-size:9px">&#9660;</span></div>
  <div class="abs catnav-item last" style="left:705px;width:125px">How it works</div>
  <div class="abs tally">So far you've Givlomarted: <b>$0</b></div>
</nav>

<section>
  <div class="abs hero" role="img" aria-label="Photo of a smiling older man with a white beard, glasses and cap, listening to headphones"></div>
  <h1 class="abs hero-title">Shop. Sell. Donate.</h1>
  <p class="abs hero-sub">A % of everything sold goes to a great cause</p>
</section>

<section>
  <div class="abs get-started">Get started...</div>

  <div class="abs action" style="left:63px">
    <svg viewBox="0 0 100 100" width="100">
      <path d="M88 6 L94 12 L92 34 L46 80 L20 54 L66 8 Z" fill="var(--teal)"/>
      <circle cx="80" cy="20" r="5" fill="#fff"/>
      <path d="M40 58 L50 68 L70 44" fill="none" stroke="#fff" stroke-width="6" stroke-linecap="round" stroke-linejoin="round"/>
      <path d="M22 60 L6 76 L20 78 L20 94 L36 78 Z" fill="var(--teal)"/>
    </svg>
    <div class="action-label" style="color:var(--teal)">Sell</div>
  </div>

  <div class="abs action" style="left:376px">
    <svg viewBox="0 0 110 90" width="110">
      <path d="M2 6 L18 6 L34 64 L96 64" fill="none" stroke="#222" stroke-width="5" stroke-linejoin="round"/>
      <path d="M20 14 L106 14 L94 52 L30 52" fill="none" stroke="#222" stroke-width="4"/>
      <line x1="24" y1="26" x2="102" y2="26" stroke="#222" stroke-width="3"/>
      <line x1="27" y1="39" x2="98" y2="39" stroke="#222" stroke-width="3"/>
      <circle cx="42" cy="78" r="7" fill="none" stroke="#222" stroke-width="4"/>
      <circle cx="88" cy="78" r="7" fill="none" stroke="#222" stroke-width="4"/>
    </svg>
    <div class="action-label" style="color:var(--ink)">Shop</div>
  </div>

  <div class="abs action" style="left:659px">
    <svg viewBox="0 0 100 90" width="100">
      <path d="M50 86 C20 64 4 48 4 28 C4 12 16 2 30 2 C40 2 46 8 50 14 C54 8 60 2 70 2 C84 2 96 12 96 28 C96 48 80 64 50 86 Z" fill="var(--red)"/>
      <path d="M50 72 C28 56 16 44 16 30 C16 20 23 14 31 14 C39 14 44 20 50 28 C56 20 61 14 69 14 C77 14 84 20 84 30 C84 44 72 56 50 72 Z" fill="#fff"/>
    </svg>
    <div class="action-label" style="color:var(--red)">Causes</div>
  </div>

  <div class="abs action" style="left:942px">
    <svg viewBox="0 0 80 80" width="80">
      <rect x="2" y="2" width="76" height="76" fill="none" stroke="var(--blue)" stroke-width="4"/>
      <path d="M4 4 L76 4 L76 22 Q67 30 58 22 Q49 30 40 22 Q31 30 22 22 Q13 30 4 22 Z" fill="var(--blue)"/>
      <path d="M10 26 L22 26 L22 76 L10 76 Z M58 26 L70 26 L70 76 L58 76 Z" fill="var(--blue)"/>
      <rect x="26" y="50" width="28" height="26" fill="var(--blue)"/>
    </svg>
    <div class="action-label" style="color:var(--blue)">Stores</div>
  </div>

  <div class="abs choose">Choose your cause...</div>

  <div class="abs cause" style="left:66px;color:#d0358a">Dry Wing Aid</div>
  <div class="abs cause" style="left:178px;color:#4a5a6a">Brainwell Fund</div>
  <div class="abs cause" style="left:283px;color:#4a2d8c">Glowlight Kids</div>
  <div class="abs cause" style="left:398px;color:#1f3e8a">Cure Circle</div>
  <div class="abs cause" style="left:505px;color:#111">Green Orbit</div>
  <div class="abs cause" style="left:625px;color:#777">Kidsworld</div>
  <div class="abs cause" style="left:722px;color:#c8102e">Child Haven</div>
  <div class="abs cause" style="left:833px;color:#0b5fa5">Paws Trust</div>
  <div class="abs cause" style="left:948px;color:#d9261c">NeuroCare</div>
  <div class="abs more">
    <svg width="15" height="15" viewBox="0 0 15 15"><path d="M5.5 0h4v5.5H15v4H9.5V15h-4V9.5H0v-4h5.5z" fill="#111"/></svg>
    More
  </div>
</section>

</body>
</html>
```